Government contracting small business needs a web design

Tarnvale Systems Inc is a veteran owned small business that delivers a full range of professional services as well as training in information technology, security and defense intelligence solutions.
We need a professional/corporate looking website where potential clients can view what services are offered.
This being a new company, there is not much that can added more than a narrative statement, stock photos and a place where potential customers and employees can make contact.
Open to ideas.
US Government
Small Business

```html
<!DOCTYPE html>
<html lang="en">
<head>
<meta charset="utf-8">
<title>Tarnvale Systems Inc</title>
<link href="https://fonts.googleapis.com/css2?family=Arimo:wght@400;700&display=swap" rel="stylesheet">
<style>
:root{
  --orange:#f47a10;
  --orange-light:#f9a23a;
  --orange-deep:#ef6a06;
  --ink:#1d1d1d;
  --nav:#4a4a4a;
  --muted:#6b6b6b;
  --rule:#9a9a9a;
  --hero:#3e3e3e;
  --hero-dark:#2c2c2c;
  --white:#ffffff;
}
*{box-sizing:border-box;margin:0;padding:0}
html,body{width:963px;height:1200px;overflow:hidden;background:var(--white)}
body{font-family:"Arimo",Arial,sans-serif;color:var(--ink);position:relative}
.page{position:relative;width:963px;height:1200px;overflow:hidden}
.header-sweep{position:absolute;left:0;top:0}
.brand{position:absolute;left:50px;top:38px;font-size:58px;font-weight:700;color:var(--white);letter-spacing:-3px;line-height:1}
.contact{position:absolute;top:28px;font-size:9.5px;line-height:20px;color:var(--muted)}
.contact.addr{left:631px}
.contact.reach{left:731px;color:var(--orange)}
.main-nav{position:absolute;top:96px;left:0;width:963px;height:20px}
.main-nav a{position:absolute;font-size:15px;font-weight:700;color:var(--nav);text-decoration:none}
.main-nav a.current{color:#7a4a1a}
.top-rule{position:absolute;left:11px;top:122px;width:952px;height:3px;background:var(--orange)}
.hero{position:absolute;left:11px;top:127px;width:952px;height:589px;background:linear-gradient(#333333,#4a4a4a 45%,#555555);overflow:hidden}
.hero-backdrop{position:absolute;left:0;top:358px;width:952px;height:231px;
  background:
    radial-gradient(ellipse 40% 60% at 8% 80%,rgba(20,20,20,.85),transparent 70%),
    radial-gradient(ellipse 40% 60% at 92% 80%,rgba(20,20,20,.85),transparent 70%),
    radial-gradient(ellipse 45% 50% at 50% 55%,#c9c9c9,transparent 75%),
    linear-gradient(#8a8a8a,#b4b4b4 35%,#7a7a7a 65%,#2a2a2a)}
.slide{position:absolute;left:142px;top:93px;width:666px;height:273px;
  background:
    radial-gradient(ellipse 35% 40% at 80% 25%,rgba(214,190,150,.55),transparent 70%),
    radial-gradient(ellipse 30% 35% at 30% 25%,rgba(160,190,210,.45),transparent 70%),
    radial-gradient(ellipse 40% 35% at 40% 75%,rgba(120,170,120,.35),transparent 70%),
    linear-gradient(#6b5d4c,#4a4036 45%,#2a2520)}
.slide-caption{position:absolute;right:0;top:169px;text-align:right}
.slide-caption .kicker{display:inline-block;background:rgba(10,10,10,.85);color:var(--orange);font-weight:700;font-size:15.5px;padding:1px 9px 2px 8px}
.slide-caption .title{display:block;background:rgba(10,10,10,.85);color:var(--white);font-weight:700;font-size:19.5px;padding:1px 9px 3px 12px}
.slide-dots{position:absolute;left:142px;top:366px;width:666px;height:40px;background:rgba(20,20,20,.8)}
.dot{position:absolute;top:14px;width:12px;height:12px;border-radius:50%;background:#e8e8e8}
.dot.active{background:var(--orange-deep)}
.service{position:absolute;top:663px;width:212px;height:79px;background:var(--white);box-shadow:0 2px 4px rgba(0,0,0,.25)}
.service .icon{position:absolute;left:9px;top:14px;width:30px;height:28px;border-radius:4px;background:linear-gradient(#d8d8d8,#7b7b7b)}
.service h3{position:absolute;right:16px;top:18px;font-size:14.5px;font-weight:700;color:var(--ink)}
.service .more{position:absolute;right:16px;top:52px;font-size:10.5px;font-weight:700;color:var(--orange);text-decoration:none}
.about{position:absolute;left:162px;top:772px;width:660px}
.about h2{font-size:17px;font-weight:700;color:var(--orange);margin-bottom:9px}
.about p{font-size:12.3px;line-height:14.8px;color:var(--ink)}
.rule{position:absolute;left:154px;width:669px;height:1px;background:var(--rule)}
.link-col{position:absolute;top:944px}
.link-col h4{font-size:14px;font-weight:400;color:var(--orange);margin-bottom:10px}
.link-col ul{list-style:none}
.link-col li{font-size:12.3px;line-height:14.8px;color:var(--ink)}
.copyright{position:absolute;left:162px;top:1107px;font-size:11.5px;line-height:14px;color:var(--muted)}
.foot-nav a{position:absolute;top:1107px;font-size:12.5px;color:var(--ink);text-decoration:none}
</style>
</head>
<body>
<div class="page">
  <svg class="header-sweep" width="963" height="640" viewBox="0 0 963 640" aria-hidden="true">
    <defs>
      <linearGradient id="sweep" x1="0" y1="0" x2="1" y2="1">
        <stop offset="0" stop-color="#f9a23a"/>
        <stop offset=".5" stop-color="#f47a10"/>
        <stop offset="1" stop-color="#ef6a06"/>
      </linearGradient>
    </defs>
    <path d="M0 0 H408 C440 60 446 200 400 330 C330 480 200 580 0 615 Z" fill="url(#sweep)"/>
  </svg>

  <div class="brand">Tarnvale</div>

  <div class="contact addr">22 Larkspur Row, 410<br>Denlow, CA 45624</div>
  <div class="contact reach">(+00) 5550 12 345<br>hello@tarnvale.example</div>

  <nav class="main-nav">
    <a class="current" href="#" style="left:366px">Home</a>
    <a href="#" style="left:445px">Company</a>
    <a href="#" style="left:546px">Services</a>
    <a href="#" style="left:632px">Projects</a>
    <a href="#" style="left:720px">Contact Us</a>
  </nav>
  <div class="top-rule"></div>

  <section class="hero">
    <div class="hero-backdrop" role="img" aria-label="Night view of a government capitol building lit by street lamps"></div>
    <div class="slide" role="img" aria-label="Operations center with analysts working at rows of monitors">
      <div class="slide-caption">
        <span class="kicker">/ INFRASTRUCTURE /</span>
        <span class="title">Cyber Security Solutions</span>
      </div>
    </div>
    <div class="slide-dots">
      <span class="dot active" style="left:296px"></span>
      <span class="dot" style="left:313px"></span>
      <span class="dot" style="left:330px"></span>
      <span class="dot" style="left:346px"></span>
      <span class="dot" style="left:363px"></span>
      <span class="dot" style="left:380px"></span>
    </div>
  </section>

  <div class="service" style="left:153px">
    <div class="icon" role="img" aria-label="Globe icon"></div>
    <h3>Cyber Security</h3>
    <a class="more" href="#">LEARN MORE</a>
  </div>
  <div class="service" style="left:382px">
    <div class="icon" role="img" aria-label="Server rack icon"></div>
    <h3>Dynamic Data Center</h3>
    <a class="more" href="#">LEARN MORE</a>
  </div>
  <div class="service" style="left:609px">
    <div class="icon" role="img" aria-label="Video monitor icon"></div>
    <h3>Full Motion Video</h3>
    <a class="more" href="#">LEARN MORE</a>
  </div>

  <section class="about">
    <h2>/ ABOUT US /</h2>
    <p>Tarnvale Systems® is one of the fastest growing information technology solutions providers in the country. Founded in 1997, the veteran-owned, privately held business has consistently grown both its revenue and its staff since the company’s inception.<br>Based in Aldermoor, CO, Tarnvale also has an office in Fairholt, VA, that houses its federal operations. Today, Tarnvale is approximately 100 employees strong, with its seasoned professionals possessing decades of experience – working in the public and private sectors – as well as top-secret security clearances.</p>
  </section>

  <div class="rule" style="top:916px"></div>

  <div class="link-col" style="left:170px">
    <h4>Company</h4>
    <ul><li>Executive Team</li><li>Corporate Values</li><li>Certifications</li><li>Clients and Partners</li><li>Government Contracting</li><li>Contact Us</li><li>Careers</li></ul>
  </div>
  <div class="link-col" style="left:355px">
    <h4>Solution Center</h4>
    <ul><li>BPM</li><li>Cyber Security</li><li>DR/COOP</li><li>Dynamic Data Center</li><li>Full Motion Video</li><li>Mobility Solutions</li><li>Virtualization</li></ul>
  </div>
  <div class="link-col" style="left:521px">
    <h4>Press and News</h4>
    <ul><li>Case Studies</li><li>Press releases</li><li>Events</li></ul>
  </div>
  <div class="link-col" style="left:688px">
    <h4>Clients &amp; Partners</h4>
    <ul><li>Clients</li><li>Integrator Partners</li><li>Partner Alliances</li></ul>
  </div>

  <div class="rule" style="top:1098px"></div>

  <div class="copyright">2012 - Tarnvale Systems Incorporated.<br>All rights reserved.</div>
  <nav class="foot-nav">
    <a href="#" style="left:464px">Home</a>
    <a href="#" style="left:531px">Company</a>
    <a href="#" style="left:615px">Services</a>
    <a href="#" style="left:687px">Projects</a>
    <a href="#" style="left:759px">Contact Us</a>
  </nav>
</div>
</body>
</html>
```